依頼詳細
【サイトの最大の要望】
・新規集客(ネット予約がゴール)
・院の認知アップ(新規開業のため)

【強み】
・お待たせしないシステム
・保険適用の漢方治療

【ターゲット】
・世代:30代以降
・性別:やや女性寄り

【完成イメージ】
全面は白で、植物などの緑、茶色・木目調を差し色にしています。
待合室については濃いめの木目調のカウンターテーブルがあり、
ペンダントライトでカフェ風な作りになっています。

・完成イメージ
http://vrview.mokunoie-kenchiku.jp/wt_movie/p_mv/48391qzpa7r/vtour/tour.html

・木乃家建築で内観がイメージに近い事例
http://www.mokunoie-kenchiku.jp/medical/doctor/example/morita_naika.html

【参考サイト】
https://www.kawabe-dining.jp/lavendora/
https://sorine-cafe.jp/
http://www.kirigaoka-tei.com/restaurant/wrencafe/
http://waffle.tovari-works.jp/
http://www.almondlodge.jp/#!page4

【サイトマップ】
1.TOP
2.初めての方へ
3.医院について
4.当院の特徴
5.院長紹介
6.よくある質問
7.ブログ(一覧)
∟8.ブログ(詳細)
9.お知らせ(一覧)
∟10.お知らせ(詳細)
11.耳の病気
12.鼻の病気
13.口・のどの病気
14.頭・顔・首の病気
15.風邪の症状
16.更年期の症状にお悩みの方
17.冷えにお悩みの方へ
18.不眠にお悩みの方へ
19.めまい・耳鳴りにお悩みの方へ
20.体質改善
希望イメージ
• シンプル
複雑
• 単色
カラフル
• 暗い
明るい
• 日常
高級
• 遊び心
厳粛
• 未来的
伝統的
• 女性的
男性的
希望する色
ベースは白。植物などの緑、木目調の濃い茶色を差し色
納品ファイル
• フォトショップ形式 (.psd)
• PNG形式 (.png)
補足説明
【店舗へのご連絡はおやめください】
ワークミツ規約にもありますが、店舗への通常業務に支障が出るため、
直接電話等のお問い合わせをお控え頂きますよう、ご協力願います。

【素材写真】
素材については、ピクセラのカンプ画像をご使用ください。
選定後に正規データをお渡し致します。
(画像はマンスリーパック内でお願い致します。)
依頼公開後の追記内容
ワイヤフレームを添付致します。
提案期間を延長致します。
提案数がないため、期限を延長致します。
こちら提案数が欲しいため、延長致します。
■ 選んだ理由

一見してシンプルながら目を引くデザインで、院のイメージに合っていたため

■ 提案者全員のお礼・コメント

この度はご提案くださり、ありがとうございました。
また機会がございましたら、どうぞ宜しくお願い致します。

```html
<!DOCTYPE html>
<html lang="ja">
<head>
<meta charset="utf-8">
<title>こもれび耳鼻咽喉科</title>
<link href="https://fonts.googleapis.com/css2?family=Noto+Sans+JP:wght@400;500;700&display=swap" rel="stylesheet">
<style>
:root{
  --brown:#6a4838;
  --brown-dark:#4e3328;
  --beige:#e9e0dc;
  --beige-pill:#e2d6d1;
  --green:#2f8a3b;
  --green-light:#d8ebda;
  --green-pill:#cfe6d2;
  --ink:#333;
  --white:#fff;
}
*{margin:0;padding:0;box-sizing:border-box}
html,body{width:1200px;height:4800px;overflow:hidden}
body{font-family:"Noto Sans JP",sans-serif;color:var(--ink);background:var(--white);position:relative}
ul{list-style:none}
.section-title{font-size:26px;font-weight:700;color:var(--ink);text-align:center;letter-spacing:2px}

/* hero */
.hero{position:absolute;top:0;left:0;width:1200px;height:660px;
  background:
    radial-gradient(ellipse 260px 320px at 1080px 360px,rgba(94,140,80,.55),rgba(94,140,80,0) 70%),
    radial-gradient(ellipse 220px 160px at 640px 420px,rgba(255,255,255,.9),rgba(255,255,255,0) 70%),
    linear-gradient(180deg,rgba(255,255,255,0) 70%,rgba(220,218,214,.8) 100%),
    linear-gradient(90deg,#3f3834 0%,#5e5550 10%,#cfcbc6 17%,#5a4538 21%,#4e3a2e 30%,#dcd8d2 35%,#f4f3f0 50%,#f7f6f3 72%,#e9ece4 86%,#dde4d6 100%)}
.brand{position:absolute;top:34px;left:30px;display:flex;align-items:center;gap:12px}
.brand-mark{width:42px;height:42px;border-radius:50%;background:var(--brown)}
.brand-name{font-size:34px;font-weight:700;color:var(--brown);letter-spacing:1px;white-space:nowrap}
.hours{border-collapse:collapse;font-size:12px;background:rgba(255,255,255,.92)}
.hours th,.hours td{border:1px solid #c9bcb5;padding:4px 8px;text-align:center}
.hours th{background:var(--brown);color:var(--white);font-weight:500}
.hours td{color:var(--brown)}
.hero .hours{position:absolute;top:20px;left:572px}
.hero-note{position:absolute;top:108px;left:572px;font-size:11px;color:var(--brown)}
.contact{position:absolute;top:12px;right:30px;text-align:left}
.contact-lead{font-size:15px;color:var(--brown)}
.contact-tel{display:flex;align-items:center;gap:10px;font-size:34px;font-weight:700;color:var(--brown);margin-top:4px}
.contact-addr{font-size:15px;color:var(--brown);margin-top:10px}
.reserve{position:absolute;left:960px;top:490px;width:130px;height:130px;border-radius:50%;background:var(--white);border:3px solid var(--brown);display:flex;flex-direction:column;align-items:center;justify-content:center;color:var(--brown);font-size:17px;font-weight:700;line-height:1.3;text-align:center}

/* nav */
.global-nav{position:absolute;top:660px;left:0;width:1200px;height:170px;display:flex;justify-content:center;align-items:center;gap:44px;font-size:16px;color:var(--ink)}

/* categories */
.category{position:absolute;left:0;width:1200px}
.category.ent{top:830px;height:420px;background:var(--beige)}
.category.kampo{top:1250px;height:410px;background:var(--green-light)}
.category .section-title{position:absolute;top:56px;width:100%}
.category.ent .section-title{color:var(--brown)}
.category.kampo .section-title{color:var(--green)}
.cat-list{position:absolute;top:150px;left:95px;display:flex;gap:46px}
.cat-item{width:170px;text-align:center;font-size:16px;line-height:1.45}
.cat-icon{width:130px;height:130px;border-radius:50%;margin:0 auto 16px;display:flex;align-items:center;justify-content:center}
.cat-icon svg{width:70px;height:70px}
.ent .cat-icon{background:var(--brown)}
.kampo .cat-icon{background:var(--green)}

/* news */
.news{position:absolute;top:1660px;left:0;width:1200px;height:590px}
.news-col{position:absolute;top:80px;width:420px}
.news-col.info{left:160px}
.news-col.blog{left:640px}
.news-head{width:340px;height:44px;margin:0 auto;border-radius:4px;display:flex;align-items:center;justify-content:center;font-size:20px;font-weight:700}
.info .news-head{background:var(--beige-pill);color:var(--brown)}
.blog .news-head{background:var(--green-pill);color:var(--green)}
.news-list{margin:46px 0 0 30px}
.news-list li{font-size:15px;height:70px;display:flex;gap:28px}
.more{position:absolute;top:440px;right:40px;display:flex;align-items:center;gap:8px;font-size:15px;font-weight:700;color:var(--ink)}

/* photo band */
.interior{position:absolute;top:2250px;left:0;width:1200px;height:370px;
  background:
    radial-gradient(ellipse 120px 90px at 420px 250px,rgba(80,130,70,.55),rgba(80,130,70,0) 70%),
    radial-gradient(ellipse 140px 80px at 660px 170px,rgba(150,190,140,.5),rgba(150,190,140,0) 70%),
    linear-gradient(180deg,rgba(255,255,255,0) 65%,rgba(210,206,200,.7) 100%),
    linear-gradient(90deg,#3d332b 0%,#8a7a66 8%,#d8d2c6 14%,#b8ab98 24%,#efeee9 32%,#f3f3ef 55%,#dfe3dc 66%,#cfcfca 76%,#5a4636 82%,#4a3a2e 100%)}

/* features */
.features{position:absolute;top:2620px;left:0;width:1200px;height:560px}
.features .section-title{position:absolute;top:62px;width:100%}
.feature-list{position:absolute;top:140px;left:90px;display:flex;gap:90px}
.feature{width:280px;text-align:center;font-size:18px;font-weight:700}
.feature-photo{width:280px;height:280px;border-radius:50%;margin-bottom:36px}

/* director */
.director{position:absolute;top:3180px;left:0;width:1200px;height:540px;background:var(--green-light)}
.director .section-title{position:absolute;top:36px;width:100%}
.director-text{position:absolute;top:135px;left:120px;width:600px;font-size:16px;line-height:1.55;color:var(--ink)}
.director-name{position:absolute;top:370px;left:120px;font-size:22px;font-weight:700;line-height:1.5}
.director-photo{position:absolute;top:150px;left:800px;width:280px;height:330px;background:linear-gradient(180deg,#e6e9ec 0%,#f4f5f6 45%,#dfe5ea 100%)}

/* access */
.access{position:absolute;top:3720px;left:0;width:1200px;height:300px}
.access .brand{top:64px;left:120px}
.access-addr{position:absolute;top:140px;left:120px;font-size:16px}
.access-tel{position:absolute;top:190px;left:120px;display:flex;align-items:center;gap:10px;font-size:30px;font-weight:700;color:var(--brown)}
.access .hours{position:absolute;top:60px;left:600px;font-size:18px}
.access .hours th,.access .hours td{padding:8px 14px}
.access-note{position:absolute;top:196px;left:610px;font-size:15px}
.map{position:absolute;top:4020px;left:0;width:1200px;height:300px;display:flex;align-items:center;justify-content:center;
  background:
    radial-gradient(ellipse 160px 110px at 600px 160px,rgba(222,170,200,.45),rgba(222,170,200,0) 75%),
    linear-gradient(135deg,#eeeeea 0%,#e4e6e2 40%,#eceae4 70%,#e2e6df 100%)}

/* footer */
.site-footer{position:absolute;top:4320px;left:0;width:1200px;height:480px;background:var(--beige)}
.footer-col{position:absolute;top:42px}
.footer-col h3{font-size:18px;font-weight:700;color:var(--brown);margin-bottom:8px}
.footer-col li{font-size:15px;line-height:1.75;padding-left:22px}
.copyright{position:absolute;bottom:0;left:0;width:1200px;height:40px;background:var(--brown-dark);color:var(--white);font-size:12px;display:flex;align-items:center;justify-content:center}
</style>
</head>
<body>

<header class="hero" role="img" aria-label="白を基調とした明るい待合室と受付カウンター、観葉植物の写真">
  <div class="brand"><span class="brand-mark"></span><span class="brand-name">こもれび耳鼻咽喉科</span></div>
  <table class="hours">
    <tr><th>診療時間</th><th>月</th><th>火</th><th>水</th><th>木</th><th>金</th><th>土</th><th>日</th></tr>
    <tr><td>09:00～13:00</td><td>●</td><td>●</td><td>●</td><td>●</td><td>●</td><td>●</td><td>／</td></tr>
    <tr><td>16:00～19:00</td><td>●</td><td>●</td><td>●</td><td>／</td><td>●</td><td>／</td><td>／</td></tr>
  </table>
  <p class="hero-note">休診日：木曜日午後・土曜日午後・日・祝</p>
  <div class="contact">
    <p class="contact-lead">ご予約・お問い合わせはこちら</p>
    <p class="contact-tel">
      <svg width="30" height="30" viewBox="0 0 24 24" aria-hidden="true"><path fill="#6a4838" d="M6.6 10.8a15.1 15.1 0 0 0 6.6 6.6l2.2-2.2a1 1 0 0 1 1-.25 11.4 11.4 0 0 0 3.6.57 1 1 0 0 1 1 1V20a1 1 0 0 1-1 1A17 17 0 0 1 3 4a1 1 0 0 1 1-1h3.5a1 1 0 0 1 1 1c0 1.25.2 2.45.57 3.6a1 1 0 0 1-.25 1z"/></svg>
      000-000-0000
    </p>
    <p class="contact-addr">〒000-0000 緑ヶ丘県若葉市本町◯◯</p>
  </div>
  <div class="reserve">ご予約は<br>こちら
    <svg width="34" height="34" viewBox="0 0 24 24" aria-hidden="true" style="margin-top:6px"><rect x="3" y="5" width="18" height="16" rx="2" fill="none" stroke="#6a4838" stroke-width="2"/><rect x="3" y="5" width="18" height="5" fill="#6a4838"/><rect x="7" y="2" width="2" height="5" fill="#6a4838"/><rect x="15" y="2" width="2" height="5" fill="#6a4838"/></svg>
  </div>
</header>

<nav class="global-nav">
  <a>初めての方へ</a><a>医院について</a><a>当院の特徴</a><a>院長紹介</a><a>耳鼻咽喉科</a><a>漢方治療</a><a>よくある質問</a>
</nav>

<section class="category ent">
  <h2 class="section-title">耳鼻咽喉科</h2>
  <ul class="cat-list">
    <li class="cat-item"><div class="cat-icon" role="img" aria-label="耳の病気のアイコン"><svg viewBox="0 0 64 64" fill="none" stroke="#fff" stroke-width="4" stroke-linecap="round"><circle cx="14" cy="32" r="5" fill="#fff" stroke="none"/><path d="M26 22a14 14 0 0 1 0 20"/><path d="M35 15a24 24 0 0 1 0 34"/><path d="M44 8a34 34 0 0 1 0 48"/></svg></div>耳の病気</li>
    <li class="cat-item"><div class="cat-icon" role="img" aria-label="鼻の病気のアイコン"><svg viewBox="0 0 64 64" fill="none" stroke="#fff" stroke-width="4" stroke-linecap="round"><path d="M8 24h32a7 7 0 1 0-7-7"/><path d="M8 34h46"/><path d="M8 44h26a7 7 0 1 1-7 7"/></svg></div>鼻の病気</li>
    <li class="cat-item"><div class="cat-icon" role="img" aria-label="口・のどの病気のアイコン"><svg viewBox="0 0 64 64" fill="none" stroke="#fff" stroke-width="4" stroke-linejoin="round"><path d="M32 8C24 22 18 30 18 40a14 14 0 0 0 28 0c0-10-6-18-14-32z"/><path d="M26 42a6 6 0 0 0 6 6" stroke-linecap="round"/></svg></div>口・のどの病気</li>
    <li class="cat-item"><div class="cat-icon" role="img" aria-label="頭・顔・首の病気のアイコン"><svg viewBox="0 0 64 64" fill="none" stroke="#fff" stroke-width="4" stroke-linejoin="round"><path d="M24 8h16v16h16v16H40v16H24V40H8V24h16z"/></svg></div>頭・顔・首の病気</li>
    <li class="cat-item"><div class="cat-icon" role="img" aria-label="風邪の症状のアイコン"><svg viewBox="0 0 64 64" fill="none" stroke="#fff" stroke-width="4" stroke-linecap="round" stroke-linejoin="round"><rect x="14" y="20" width="36" height="26" rx="7"/><path d="M14 26H6v14h8M50 26h8v14h-8"/><path d="M20 29h24M20 37h24"/></svg></div>風邪の症状</li>
  </ul>
</section>

<section class="category kampo">
  <h2 class="section-title">漢方治療</h2>
  <ul class="cat-list">
    <li class="cat-item"><div class="cat-icon" role="img" aria-label="更年期の症状のアイコン"><svg viewBox="0 0 64 64"><path fill="#fff" d="M32 54 10 32A12 12 0 0 1 32 16a12 12 0 0 1 22 16z"/></svg></div>更年期の症状に<br>お悩みの方へ</li>
    <li class="cat-item"><div class="cat-icon" role="img" aria-label="冷えのアイコン"><svg viewBox="0 0 64 64" fill="none" stroke="#fff" stroke-width="4" stroke-linecap="round"><path d="M32 6v52M9.5 19l45 26M9.5 45l45-26"/><path d="M26 10l6 6 6-6M26 54l6-6 6 6"/></svg></div>冷えに<br>お悩みの方へ</li>
    <li class="cat-item"><div class="cat-icon" role="img" aria-label="不眠のアイコン"><svg viewBox="0 0 64 64"><path fill="#fff" d="M36 8a22 22 0 1 0 20 32A18 18 0 1 1 36 8z"/><path d="M44 12h10l-10 12h10" fill="none" stroke="#fff" stroke-width="3" stroke-linejoin="round"/></svg></div>不眠に<br>お悩みの方へ</li>
    <li class="cat-item"><div class="cat-icon" role="img" aria-label="めまい・耳鳴りのアイコン"><svg viewBox="0 0 64 64" fill="none" stroke="#fff" stroke-width="4" stroke-linecap="round"><path d="M32 32a4 4 0 0 1 8 0 8 8 0 0 1-16 0 12 12 0 0 1 24 0 16 16 0 0 1-32 0 20 20 0 0 1 40 0"/></svg></div>めまい・耳鳴りに<br>お悩みの方へ</li>
    <li class="cat-item"><div class="cat-icon" role="img" aria-label="体質改善のアイコン"><svg viewBox="0 0 64 64" fill="none" stroke="#fff" stroke-width="4" stroke-linecap="round" stroke-linejoin="round"><path d="M14 50C14 24 30 12 54 10c0 26-14 40-38 40z"/><path d="M14 50 40 24"/></svg></div>体質改善</li>
  </ul>
</section>

<section class="news">
  <div class="news-col info">
    <h2 class="news-head">Infomation</h2>
    <ul class="news-list">
      <li><span>yyyy/mm/dd</span><span>お知らせタイトル①</span></li>
      <li><span>yyyy/mm/dd</span><span>お知らせタイトル②</span></li>
      <li><span>yyyy/mm/dd</span><span>お知らせタイトル③</span></li>
      <li><span>yyyy/mm/dd</span><span>お知らせタイトル④</span></li>
    </ul>
    <a class="more">一覧へ <svg width="22" height="22" viewBox="0 0 22 22" aria-hidden="true"><circle cx="11" cy="11" r="11" fill="#333"/><path d="M9 6l5 5-5 5" fill="none" stroke="#fff" stroke-width="2"/></svg></a>
  </div>
  <div class="news-col blog">
    <h2 class="news-head">Blog</h2>
    <ul class="news-list">
      <li><span>yyyy/mm/dd</span><span>ブログタイトル①</span></li>
      <li><span>yyyy/mm/dd</span><span>ブログタイトル②</span></li>
      <li><span>yyyy/mm/dd</span><span>ブログタイトル③</span></li>
      <li><span>yyyy/mm/dd</span><span>ブログタイトル④</span></li>
    </ul>
    <a class="more">一覧へ <svg width="22" height="22" viewBox="0 0 22 22" aria-hidden="true"><circle cx="11" cy="11" r="11" fill="#2f8a3b"/><path d="M9 6l5 5-5 5" fill="none" stroke="#fff" stroke-width="2"/></svg></a>
  </div>
</section>

<div class="interior" role="img" aria-label="木目調の家具とペンダントライトのある待合室の写真"></div>

<section class="features">
  <h2 class="section-title">当院の特徴</h2>
  <ul class="feature-list">
    <li class="feature"><div class="feature-photo" role="img" aria-label="スマートフォンを操作する手元の写真" style="background:radial-gradient(circle at 55% 45%,#3a3a3a 0%,#3a3a3a 14%,#e3c4ad 22%,#cfb29b 40%,#a9b09a 70%,#7f8a72 100%)"></div>お待たせしないシステム</li>
    <li class="feature"><div class="feature-photo" role="img" aria-label="器に盛られた生薬の写真" style="background:radial-gradient(circle at 35% 35%,#e8d2a4 0%,#c98a4e 30%,#a5402c 60%,#7a2e20 100%)"></div>保険適用の漢方治療</li>
    <li class="feature"><div class="feature-photo" role="img" aria-label="明るく落ち着いた待合室の写真" style="background:linear-gradient(90deg,#cfc8bc 0%,#f3f2ee 35%,#e6ebe3 60%,#8d7a66 100%)"></div>カフェ風の待合室</li>
  </ul>
</section>

<section class="director">
  <h2 class="section-title">院長紹介</h2>
  <p class="director-text">院長の経歴や挨拶などの紹介文を掲載します。テキストが入ります。地域の皆さまの耳・鼻・のどの健康を守るため、丁寧な診療を心がけています。どうぞお気軽にご相談ください。院長の経歴や挨拶などの紹介文を掲載します。</p>
  <p class="director-name">こもれび耳鼻咽喉科<br>院長　院長の名前</p>
  <div class="director-photo" role="img" aria-label="白衣を着た院長のポートレート写真"></div>
</section>

<section class="access">
  <div class="brand"><span class="brand-mark"></span><span class="brand-name">こもれび耳鼻咽喉科</span></div>
  <p class="access-addr">〒000-0000 緑ヶ丘県若葉市本町◯◯</p>
  <p class="access-tel">
    <svg width="28" height="28" viewBox="0 0 24 24" aria-hidden="true"><path fill="#6a4838" d="M6.6 10.8a15.1 15.1 0 0 0 6.6 6.6l2.2-2.2a1 1 0 0 1 1-.25 11.4 11.4 0 0 0 3.6.57 1 1 0 0 1 1 1V20a1 1 0 0 1-1 1A17 17 0 0 1 3 4a1 1 0 0 1 1-1h3.5a1 1 0 0 1 1 1c0 1.25.2 2.45.57 3.6a1 1 0 0 1-.25 1z"/></svg>
    000-000-0000
  </p>
  <table class="hours">
    <tr><th>診療時間</th><th>月</th><th>火</th><th>水</th><th>木</th><th>金</th><th>土</th><th>日</th></tr>
    <tr><td>00:00～13:00</td><td>●</td><td>●</td><td>●</td><td>●</td><td>●</td><td>●</td><td>／</td></tr>
    <tr><td>16:00～19:00</td><td>●</td><td>●</td><td>●</td><td>／</td><td>●</td><td>／</td><td>／</td></tr>
  </table>
  <p class="access-note">休診日：木曜日午後・土曜日午後・日・祝</p>
</section>

<div class="map" role="img" aria-label="医院周辺の地図">
  <svg width="40" height="56" viewBox="0 0 24 34" aria-hidden="true"><path fill="#c0392b" d="M12 0a12 12 0 0 0-12 12c0 9 12 22 12 22s12-13 12-22A12 12 0 0 0 12 0z"/><circle cx="12" cy="12" r="4.5" fill="#fff"/></svg>
</div>

<footer class="site-footer">
  <div class="footer-col" style="left:100px">
    <h3>Sitemap</h3>
    <ul><li>TOP</li><li>初めての方へ</li><li>医院について</li><li>当院の特徴</li><li>院長紹介</li><li>よくある質問</li><li>ブログ</li><li>お知らせ</li></ul>
  </div>
  <div class="footer-col" style="left:430px">
    <h3>耳鼻咽喉科</h3>
    <ul><li>耳の病気</li><li>鼻の病気</li><li>口・のどの病気</li><li>頭・顔・首の病気</li><li>風邪の症状</li></ul>
  </div>
  <div class="footer-col" style="left:750px">
    <h3>漢方治療</h3>
    <ul><li>更年期の症状にお悩みの方</li><li>冷えにお悩みの方へ</li><li>不眠にお悩みの方へ</li><li>めまい・耳鳴りにお悩みの方へ</li><li>体質改善</li></ul>
  </div>
  <p class="copyright">Copyright © こもれび耳鼻咽喉科 All Rights Reserved.</p>
</footer>

</body>
</html>
```